Online Marketplace Startup for Community Facilities (Vondaloft)

A innovative, modern website design is required for a new startup called Vondaloft. Vondaloft will be an online marketplace for searching for and booking community facilities, such as schools facilities (sports grounds, halls, classrooms etc.), churches, hospitals and other community facilities.

The attached brief has been created to provide guidance on the structure and content required.

The web design shall feature a modern, innovative but user friendly interface similar style to other web start up pages:
www.hirewendle.co.uk
www.trundlo.com.au
www.markplinth.com.au

The web design shall be ‘wordpress’ compliant and allow for future functionality to be added and coded (e.g. animations, flash, blogs etc) and content to be editable.

The following brief has been created to provide guidance on the structure and content required.

An existing logo developed for Vondaloft shall be utilised and incorporated in the top left hand cover of the cover landing page (refer to attached logo designs).

Refer to attached 'Website brief' for more details on requirements.
Updates

Project Deadline Extended
Reason: I wish to grant an extension to the deadline to provide designers with more time to submit their designs.

Target Market(s)

VondaLoft will focus on building a customer network of both community facility owners (schools, hospitals, churches) and hirers (non-government organisations, community groups, event management companies, commercial businesses). Members of the general public will also be encouraged to book facilities for private functions.

Industry/Entity Type

Community

Coding

Coded - Design and coding required

Number of Pages Required

5+ page

Font styles to use
Sans Serif

Colors
3176b5
ffffff
85cae6
33a6d7

Requirements
Must have
• The web design shall feature a modern, innovative but user friendly interface similar style to other web start up pages:
• www.hirewendle.co.uk
• www.trundlo.com.au
• www.markplinth.com.au
• The web design shall be ‘wordpress’ compliant and allow for future functionality to be added and coded (e.g. animations, flash, blogs etc) and content to be editable.
• Refer to Project brief for other requirements
Nice to have
• Refer to Project brief
Should not have
• Refer to Project brief

```html
<!DOCTYPE html>
<html lang="en">
<head>
<meta charset="utf-8">
<title>VondaLoft — Community Facility Bookings</title>
<link href="https://fonts.googleapis.com/css2?family=Montserrat:wght@400;600;700;800&family=Open+Sans:wght@400;600&display=swap" rel="stylesheet">
<style>
:root{
  --navy:#1f3d78;
  --navy-deep:#1b3261;
  --navy-bar:#172a52;
  --blue:#3176b5;
  --sky:#85cae6;
  --cyan:#33a6d7;
  --tile-blue:#3a8fd6;
  --tile-pink:#e06aa6;
  --tile-yellow:#f4d20c;
  --tile-orange:#f49a12;
  --ink:#1f3d78;
  --text:#666;
  --white:#fff;
  --line:#e3e6ec;
}
*{margin:0;padding:0;box-sizing:border-box}
html,body{width:1200px;height:4545px;overflow:hidden}
body{font-family:"Open Sans",Arial,sans-serif;color:var(--text);background:var(--white);position:relative}
.abs{position:absolute}
h1,h2,h3,.brand,.nav a,.btn{font-family:"Montserrat",Arial,sans-serif}

/* header */
.site-header{left:0;top:0;width:1200px;height:106px;background:var(--white)}
.brand{display:flex;align-items:center;gap:10px;font-weight:600;color:var(--navy);font-size:28px}
.brand-mark{width:22px;height:22px;background:var(--navy)}
.site-header .brand{left:67px;top:20px}
.social{display:flex;gap:14px}
.social span{width:14px;height:14px;border-radius:50%;display:block}
.site-header .social{right:67px;top:30px}
.site-header .social span:nth-child(1){background:#3b5998}
.site-header .social span:nth-child(2){background:#55acee}
.site-header .social span:nth-child(3){background:#e4405f}
.site-header .social span:nth-child(4){background:#0e76a8}
.nav{left:67px;top:76px;width:1066px;height:76px;background:var(--navy);display:flex;justify-content:center;align-items:center;gap:44px;z-index:3}
.nav a{color:var(--white);text-decoration:none;font-size:16px;font-weight:500;letter-spacing:1px}

/* hero */
.hero{left:0;top:106px;width:1200px;height:597px;background:linear-gradient(100deg,#2c5c9c 0%,#3b6fae 45%,#2e5f9e 70%,#23457f 100%)}
.hero-kicker{left:0;width:1200px;top:190px;text-align:center;color:#d9e6f5;font-size:13px;letter-spacing:4px}
.hero h1{left:0;width:1200px;top:235px;text-align:center;color:var(--white);font-size:38px;font-weight:700;line-height:54px}
.hero .btn{left:545px;top:378px;width:142px;height:50px}
.btn{background:var(--navy);color:var(--white);font-size:13px;font-weight:600;letter-spacing:1px;display:flex;align-items:center;justify-content:center;text-transform:uppercase}
.hero-arrow{top:246px;width:20px;height:34px}
.signup{left:18px;top:395px;color:#e2ecf8}
.signup .rule{width:50px;height:2px;background:#cfe0f3;margin-bottom:34px}
.signup h3{font-size:12px;letter-spacing:5px;font-weight:600;margin:0 0 12px}
.signup p{font-size:13px;line-height:21px;width:320px}

/* tiles */
.tiles{left:0;top:703px;width:1200px;height:227px;display:flex}
.tile{width:300px;height:227px;color:var(--white);text-align:center;font-size:16px;line-height:30px;padding-top:36px}
.tile svg{display:block;margin:0 auto 22px}
.tile.blue{background:var(--tile-blue)}
.tile.pink{background:var(--tile-pink)}
.tile.yellow{background:var(--tile-yellow)}
.tile.orange{background:var(--tile-orange)}

/* about */
.about{left:0;top:930px;width:1200px;height:524px}
.section-title{width:1200px;text-align:center;color:var(--ink);font-size:46px;font-weight:700;letter-spacing:-1px}
.section-sub{width:1200px;text-align:center;color:var(--navy);font-size:13px;font-weight:700;letter-spacing:1px;font-family:"Montserrat",sans-serif}
.about p{left:260px;width:680px;text-align:center;font-size:14px;line-height:26px}

/* benefits */
.benefits{left:0;top:1454px;width:1200px;height:706px;background:var(--navy)}
.benefits-photo{left:0;top:0;width:600px;height:706px;background:linear-gradient(120deg,#b99478 0%,#6a6f78 40%,#3f4a60 70%,#c8c5c0 100%)}
.benefits h2{left:660px;top:100px;color:var(--white);font-size:44px;font-weight:700;letter-spacing:-1px}
.benefits .lead{left:660px;top:166px;color:#4f6fa5;font-size:16px}
.benefit-list{left:660px;top:236px;width:490px;list-style:none}
.benefit-list li{position:relative;padding-left:36px;color:#e4ebf6;font-size:16px;line-height:24px;margin-bottom:25px}
.benefit-list li svg{position:absolute;left:0;top:5px}
.benefits .btn{left:660px;top:543px;width:200px;height:54px;background:var(--sky);color:var(--white)}

/* pricing */
.pricing{left:0;top:2160px;width:1200px;height:961px;background:#f5f6f8}
.card{top:252px;width:334px;height:497px;background:var(--white);border:1px solid var(--line);text-align:center;color:#444}
.card.featured{border:4px solid var(--blue)}
.card h3{margin-top:56px;color:var(--ink);font-size:24px;font-weight:700}
.price{margin-top:16px;color:var(--ink);font-family:"Montserrat",sans-serif;font-weight:800;font-size:66px;line-height:66px;letter-spacing:-2px}
.price sup{font-size:30px;vertical-align:18px;margin-right:4px}
.per{color:#c2c8d4;font-size:12px;margin-top:4px}
.features{list-style:none;margin:34px auto 0;width:290px;font-size:14px;line-height:22px}
.features li{margin-bottom:24px}
.card .btn{position:absolute;left:78px;bottom:46px;width:178px;height:54px}
.note{width:1200px;text-align:center;font-size:13px;color:#777}

/* contact */
.contact{left:0;top:3121px;width:1200px;height:969px;background:linear-gradient(110deg,#1a2a4a 0%,#3d6ea8 45%,#264d86 70%,#5e86b8 100%)}
.contact-panel{left:248px;top:106px;width:707px;height:788px;background:rgba(31,61,120,.95)}
.contact-panel .kicker{left:0;top:116px;width:707px;text-align:center;color:#d5e0f0;font-size:12px;letter-spacing:2px}
.contact-panel h2{left:0;top:164px;width:707px;text-align:center;color:var(--white);font-size:46px;font-weight:700;letter-spacing:-1px}
.field{background:var(--white);color:#999;font-size:14px;padding:14px 16px}
.contact-panel .btn{left:239px;top:620px;width:222px;height:58px;background:#2b4f8c}

/* footer */
.site-footer{left:0;top:4090px;width:1200px;height:394px;background:var(--navy-deep);text-align:center;color:#93a5c6;font-size:14px}
.site-footer .brand{left:0;width:1200px;justify-content:center;top:78px;color:var(--white)}
.site-footer .brand-mark{background:var(--white)}
.site-footer p{left:250px;width:700px;line-height:24px}
.bottom-bar{left:0;top:4484px;width:1200px;height:61px;background:var(--navy-bar);color:#8798b8;font-size:12px}
.bottom-bar .copy{left:67px;top:22px}
.bottom-bar .social{right:67px;top:24px}
.bottom-bar .social span{width:12px;height:12px;background:#8798b8}
</style>
</head>
<body>

<header class="site-header abs">
  <div class="brand abs"><span class="brand-mark"></span>VondaLoft</div>
  <div class="social abs"><span></span><span></span><span></span><span></span></div>
</header>
<nav class="nav abs">
  <a>Home</a><a>About</a><a>How It Works</a><a>Services</a><a>Packages</a><a>Why Us?</a><a>News</a><a>FAQ</a><a>Contact</a>
</nav>

<section class="hero abs" role="img" aria-label="Photo of a smiling woman working on a laptop, blue tinted">
  <div class="hero-kicker abs">WELCOME TO VONDALOFT</div>
  <h1 class="abs">Utilising your facility to create value<br>for your organisation and the community</h1>
  <div class="btn abs">Get Started</div>
  <svg class="hero-arrow abs" style="left:30px" viewBox="0 0 20 34"><path d="M17 2 3 17l14 15" fill="none" stroke="#fff" stroke-width="3"/></svg>
  <svg class="hero-arrow abs" style="right:30px" viewBox="0 0 20 34"><path d="M3 2l14 15L3 32" fill="none" stroke="#fff" stroke-width="3"/></svg>
  <div class="signup abs">
    <div class="rule"></div>
    <h3>SIGN UP TODAY</h3>
    <p>Let us help you bring out value from your facility with our online platform</p>
  </div>
</section>

<section class="tiles abs">
  <div class="tile blue">
    <svg width="70" height="64" viewBox="0 0 70 64"><path d="M8 24h12l30-16v48L20 40H8z" fill="#fff"/><path d="M20 40l6 18h8l-6-18" fill="#fff"/><path d="M56 22l8-6M58 32h10M56 42l8 6" stroke="#fff" stroke-width="3"/></svg>
    Marketing and Promotion of<br>your Facility
  </div>
  <div class="tile pink">
    <svg width="70" height="64" viewBox="0 0 70 64"><rect x="18" y="4" width="34" height="56" fill="none" stroke="#fff" stroke-width="3"/><path d="M25 16h20M25 24h20M25 32h20M25 40h20M25 48h14" stroke="#fff" stroke-width="3"/></svg>
    Administer bookings and<br>enquiries
  </div>
  <div class="tile yellow">
    <svg width="70" height="64" viewBox="0 0 70 64"><rect x="16" y="6" width="38" height="52" rx="3" fill="#fff"/><circle cx="35" cy="28" r="11" fill="none" stroke="#f4d20c" stroke-width="3"/><path d="M24 48h22" stroke="#f4d20c" stroke-width="3"/></svg>
    Invoice and Payment<br>collection
  </div>
  <div class="tile orange">
    <svg width="70" height="64" viewBox="0 0 70 64"><rect x="16" y="4" width="38" height="56" fill="#fff"/><rect x="22" y="36" width="6" height="16" fill="#f49a12"/><rect x="32" y="28" width="6" height="24" fill="#f49a12"/><rect x="42" y="20" width="6" height="32" fill="#f49a12"/></svg>
    Bookings reports and<br>customer service
  </div>
</section>

<section class="about abs">
  <h2 class="section-title abs" style="top:52px">who we are</h2>
  <div class="section-sub abs" style="top:126px">OUR STORY AND WHAT WE DO</div>
  <p class="abs" style="top:210px">VondaLoft will focus on building a customer network of both community facility owners (schools, hospitals, churches) and hirers (non-government organisations, community groups, event management companies, commercial businesses). Members of the general public will also be encouraged to book facilities for private functions.</p>
  <p class="abs" style="top:340px">VondaLoft is a start-up recently formed in 2017 in Melbourne, Australia by husband and wife co-founders, Mo and Kit.</p>
</section>

<section class="benefits abs">
  <div class="benefits-photo abs" role="img" aria-label="Photo of a smiling man in a checked shirt working at a laptop"></div>
  <h2 class="abs">The Key Benefits</h2>
  <div class="lead abs">Have reasons to sign up with VondaLoft</div>
  <ul class="benefit-list abs">
    <li><svg width="18" height="14" viewBox="0 0 18 14"><path d="M2 7l5 5L16 2" fill="none" stroke="#fff" stroke-width="3"/></svg>Use of existing, underutilised facilities</li>
    <li><svg width="18" height="14" viewBox="0 0 18 14"><path d="M2 7l5 5L16 2" fill="none" stroke="#fff" stroke-width="3"/></svg>Reduction in administrative time and cost</li>
    <li><svg width="18" height="14" viewBox="0 0 18 14"><path d="M2 7l5 5L16 2" fill="none" stroke="#fff" stroke-width="3"/></svg>Unregulated revenue stream; low setup fee</li>
    <li><svg width="18" height="14" viewBox="0 0 18 14"><path d="M2 7l5 5L16 2" fill="none" stroke="#fff" stroke-width="3"/></svg>Managed via a simple, proven and transparent online bookings system</li>
    <li><svg width="18" height="14" viewBox="0 0 18 14"><path d="M2 7l5 5L16 2" fill="none" stroke="#fff" stroke-width="3"/></svg>Potential for developing marketing and promotional opportunities and establishing commercial relationships</li>
  </ul>
  <div class="btn abs">Get Started →</div>
</section>

<section class="pricing abs">
  <h2 class="section-title abs" style="top:78px">pricing.</h2>
  <div class="section-sub abs" style="top:148px">AFFORDABLE PACKAGES FOR YOUR FACILITY</div>

  <div class="card abs" style="left:67px">
    <h3>basic</h3>
    <div class="price"><sup>$</sup>20</div>
    <div class="per">per month</div>
    <ul class="features">
      <li>Hosting of facility bookings page on VondaLoft website</li>
      <li>Training and Setup of Software System</li>
      <li>Maintenance and Support of system during term of use</li>
    </ul>
    <div class="btn">Purchase →</div>
  </div>
  <div class="card featured abs" style="left:433px">
    <h3>standard *</h3>
    <div class="price"><sup>$</sup>40</div>
    <div class="per">per month</div>
    <ul class="features">
      <li>Hosting, training, setup and maintenance of software system during term of use</li>
      <li>Marketing of facility to external hirers</li>
      <li>Additional Admin and support</li>
    </ul>
    <div class="btn" style="background:var(--blue)">Purchase →</div>
  </div>
  <div class="card abs" style="left:797px">
    <h3>premium**</h3>
    <div class="price"><sup>$</sup>100</div>
    <div class="per">per month</div>
    <ul class="features">
      <li>Hosting, setup, maintenance and admin support of software system</li>
      <li>Marketing of facility to external hirer</li>
      <li>On site supervision of activities Sponsorships and Event Management</li>
    </ul>
    <div class="btn">Purchase →</div>
  </div>

  <div class="note abs" style="top:782px">* Recommended package</div>
  <div class="note abs" style="top:812px">** Not yet available</div>
</section>

<section class="contact abs" role="img" aria-label="Close-up photo of a hand holding a smartphone over a keyboard, blue tinted">
  <div class="contact-panel abs">
    <div class="kicker abs">PLEASE USE THE FORM BELOW TO SEND US YOUR INQUIRY</div>
    <h2 class="abs">Talk to Us</h2>
    <div class="field abs" style="left:69px;top:245px;width:168px;height:52px">Name</div>
    <div class="field abs" style="left:269px;top:245px;width:168px;height:52px">Email</div>
    <div class="field abs" style="left:469px;top:245px;width:168px;height:52px">Subject</div>
    <div class="field abs" style="left:69px;top:339px;width:568px;height:215px">Message</div>
    <div class="btn abs">Send Message</div>
  </div>
</section>

<footer class="site-footer abs">
  <div class="brand abs"><span class="brand-mark"></span>VondaLoft</div>
  <p class="abs" style="top:144px">The VondaLoft online platform is a convenient and highly functional marketplace for searching and booking community facilities (schools, churches, health care facilities).</p>
  <p class="abs" style="top:220px">PO Box 4471, Larchfield VIC 3190, Australia</p>
  <p class="abs" style="top:251px">040 555 0192</p>
</footer>
<div class="bottom-bar abs">
  <div class="copy abs">Copyright 2017 VondaLoft. All Rights Reserved.</div>
  <div class="social abs"><span></span><span></span><span></span><span></span></div>
</div>

</body>
</html>
```